" Atendemos de maneira integrada em reabilitação ,tanto odontológica como neurológica. Somos terapia ocupacional, fonoaudiologia, neuropediatria e odontologia. Trabalhamos com técnicas de ponta e muito proximidade com nossos pacientes e suas famílias. "

```html
<!DOCTYPE html>
<html lang="pt-BR">
<head>
<meta charset="utf-8">
<title>Vitalize — Pasta institucional</title>
<link href="https://fonts.googleapis.com/css2?family=Montserrat:wght@400;700&display=swap" rel="stylesheet">
<style>
  :root{
    --bg:#ecebe8;
    --paper:#ffffff;
    --navy:#123f68;
    --navy-deep:#0b2c4c;
    --navy-light:#1c5a8a;
    --green:#7fc24a;
    --teal:#3fa9c9;
    --ghost:#e4e6e8;
    --ink:#6b6b6b;
  }
  *{margin:0;padding:0;box-sizing:border-box}
  html,body{width:1200px;height:1200px;overflow:hidden;background:var(--bg)}
  body{font-family:"Montserrat",Arial,sans-serif;position:relative}
  .folder{position:absolute;left:192px;top:228px;width:828px;height:756px;box-shadow:0 6px 18px rgba(0,0,0,.18)}
  .panel-inside{position:absolute;left:0;top:0;width:398px;height:756px;background:var(--paper);overflow:hidden}
  .watermark{position:absolute;left:40px;top:70px;width:300px;height:300px;border-radius:50%;background:radial-gradient(circle,var(--ghost) 0%,#f3f4f5 70%,var(--paper) 100%)}
  .contact{position:absolute;right:26px;top:440px;text-align:right;font-size:7px;line-height:11px;color:var(--ink)}
  .pocket{position:absolute;left:0;bottom:0;width:398px;height:200px}
  .pocket-brand{position:absolute;left:30px;bottom:70px;transform:rotate(180deg);transform-origin:center;width:230px;text-align:left;color:#fff}
  .panel-cover{position:absolute;left:398px;top:0;width:430px;height:756px;background:linear-gradient(90deg,var(--navy-deep) 0%,var(--navy) 40%,var(--navy-light) 100%)}
  .brand{position:absolute;left:100px;top:330px;color:#fff;text-align:left}
  .brand-mark{width:22px;height:22px;border-radius:50%;background:var(--teal);margin:0 0 12px 40px}
  .brand-name{font-weight:700;font-size:30px;letter-spacing:1px;line-height:1}
  .brand-partners{font-weight:400;font-size:12px;margin-top:5px;color:#cfe4f2}
  .pocket-brand .brand-name{font-size:16px}
  .pocket-brand .brand-partners{font-size:7px;margin-top:3px}
  .pocket-brand .brand-mark{width:12px;height:12px;margin:0 0 0 0;display:inline-block}
</style>
</head>
<body>
  <div class="folder">
    <section class="panel-inside">
      <div class="watermark" role="img" aria-label="Marca da clínica em marca-d'água clara"></div>
      <address class="contact">
        vitalize<br>
        contato@vitalize.com<br>
        (00) 0000-0000<br>
        Rua das Acácias, 120 - Centro<br>
        Cidade - UF
      </address>
      <svg class="pocket" viewBox="0 0 398 200" aria-hidden="true">
        <defs>
          <linearGradient id="pocketFill" x1="0" x2="1" y1="0" y2="0">
            <stop offset="0" stop-color="#1c5a8a"/>
            <stop offset="1" stop-color="#0b2c4c"/>
          </linearGradient>
        </defs>
        <rect x="0" y="0" width="398" height="2" fill="var(--green)"/>
        <path d="M0 4 H150 C280 4 360 80 398 200 H0 Z" fill="url(#pocketFill)"/>
      </svg>
      <div class="pocket-brand">
        <div class="brand-name">VITALIZE <span class="brand-mark"></span></div>
        <div class="brand-partners">Lúcia Andrade &amp; Paulo Serra</div>
      </div>
    </section>
    <section class="panel-cover">
      <div class="brand">
        <div class="brand-mark"></div>
        <div class="brand-name">VITALIZE</div>
        <div class="brand-partners">Lúcia Andrade &amp; Paulo Serra</div>
      </div>
    </section>
  </div>
</body>
</html>
```